Brandvik Electric - Net Link

Need a front / back flyer for our Data Communication & Low Voltage department.
Website: https://brandvikelectric.example/data-communications/
Email: NetLink@Brandvikelectric.example
Front page have data image similar to the attached but not the same picture. I don't want to use the picture from the our website, something different. Also the Brandvik logo attached.
Back page to have water mark of downtown San Francisco, description of NetLink services, listed on Website, contact information with License # 573106 and Dir # 300928451

```html
<!DOCTYPE html>
<html lang="en">
<head>
<meta charset="utf-8">
<title>Brandvik Electric – Net Link Flyer</title>
<link rel="stylesheet" href="https://fonts.googleapis.com/css2?family=Ubuntu:wght@300;400;500;700&family=Open+Sans:wght@400&display=swap">
<style>
  :root {
    --canvas: #ffffff;
    --navy-deep: #0a1a3f;
    --brand-blue: #0d4fa8;
    --icon-blue: #1e6fd6;
    --strip-purple: #4a1c7a;
    --ink: #1a1f2e;
    --white: #ffffff;
    --muted: #c9d4ea;
  }
  * { margin: 0; padding: 0; box-sizing: border-box; }
  html, body { width: 1200px; height: 2965px; overflow: hidden; background: var(--canvas); }
  body { position: relative; font-family: "Ubuntu", sans-serif; color: var(--ink); }

  .page {
    position: absolute; left: 67px; width: 1066px; height: 1378px;
    overflow: hidden;
    box-shadow: 0 14px 40px rgba(20, 30, 60, 0.18);
  }
  .page--front { top: 79px; background: linear-gradient(160deg, #ffffff 0%, #f1f3f8 60%, #e9edf4 100%); }
  .page--back { top: 1522px; background: #ffffff; }

  /* Front */
  .front-strip {
    position: absolute; left: 0; top: 0; width: 317px; height: 100%;
    background: linear-gradient(180deg, #0b0b2e 0%, #1a2a6b 30%, #21104a 60%, var(--strip-purple) 85%, #1a0f3c 100%);
  }
  .front-visual {
    position: absolute; left: 60px; top: 130px; width: 1006px; height: 800px;
    background:
      radial-gradient(ellipse 38% 30% at 40% 62%, rgba(70, 90, 220, 0.55) 0%, rgba(70, 90, 220, 0) 100%),
      linear-gradient(135deg, rgba(255,255,255,0) 32%, rgba(150, 80, 225, 0.35) 46%, rgba(60, 205, 240, 0.4) 56%, rgba(255,255,255,0) 70%);
  }
  .brand-mark {
    position: absolute; left: 0; width: 100%; top: 95px; text-align: center;
    font-weight: 700; font-size: 42px; color: var(--brand-blue); letter-spacing: 1px;
  }
  .brand-mark__square {
    display: inline-block; width: 22px; height: 22px; background: var(--brand-blue);
    margin-right: 14px; vertical-align: 2px;
  }
  .front-photo {
    position: absolute; left: 598px; top: 557px; width: 400px; height: 248px;
    border-radius: 40px;
    background: linear-gradient(180deg, #3f86d4 0%, #8cbbe6 45%, #9aa4ad 70%, #6d7580 100%);
  }
  .front-band { position: absolute; left: 0; top: 830px; width: 1066px; height: 250px; }
  .front-title {
    position: absolute; left: 280px; top: 893px;
    border-left: 5px solid #3e7bf0; padding-left: 24px;
    font-weight: 700; font-size: 53px; line-height: 62px; color: var(--white);
  }
  .contact-list { position: absolute; left: 376px; top: 1247px; list-style: none; }
  .contact-list li {
    display: flex; align-items: center; gap: 14px; height: 40px;
    font-size: 26px; letter-spacing: 2px; color: var(--ink);
  }
  .contact-list svg { width: 22px; height: 22px; }

  /* Back */
  .back-photo {
    position: absolute; left: 0; top: 0; width: 100%; height: 620px;
    background: linear-gradient(180deg, #2f7fd0 0%, #8cc0ec 35%, #b9c2c9 60%, #d9d6cf 85%, #ffffff 100%);
  }
  .services-panel {
    position: absolute; left: 61px; top: 560px; width: 943px; height: 560px;
    background: var(--navy-deep); border-radius: 62px 62px 0 0;
  }
  .service { position: absolute; display: flex; gap: 18px; color: var(--white); }
  .service__icon {
    flex: 0 0 84px; width: 84px; height: 84px; border-radius: 50%;
    background: var(--icon-blue); border: 4px solid #ffffff;
    display: flex; align-items: center; justify-content: center; margin-top: 6px;
  }
  .service__icon svg { width: 40px; height: 40px; }
  .service__title { font-weight: 700; font-size: 27px; line-height: 31px; margin-bottom: 4px; }
  .service__text { font-family: "Open Sans", sans-serif; font-size: 15.5px; line-height: 19px; color: var(--muted); }
  .service--pm { left: 50px; top: 54px; width: 420px; }
  .service--truck { left: 495px; top: 54px; width: 420px; }
  .service--cad { left: 50px; top: 211px; width: 420px; }
  .service--voice { left: 495px; top: 211px; width: 420px; }
  .service--cabling { left: 167px; top: 382px; width: 560px; }

  .back-band { position: absolute; left: 0; top: 1075px; width: 1066px; height: 250px; }
  .emergency {
    position: absolute; left: 259px; top: 1141px; width: 546px; height: 110px;
    border-left: 1px solid rgba(255,255,255,0.4); border-bottom: 1px solid rgba(255,255,255,0.4);
    display: flex; align-items: center; gap: 26px; padding-left: 24px; color: var(--white);
  }
  .emergency::after {
    content: ""; position: absolute; right: 0; top: 0; width: 120px; height: 40px;
    border-top: 1px solid rgba(255,255,255,0.4); border-right: 1px solid rgba(255,255,255,0.4);
  }
  .emergency svg { width: 48px; height: 48px; }
  .emergency__lines { font-size: 35px; line-height: 41px; font-weight: 300; }
  .emergency__number { font-weight: 700; }
  .back-footer {
    position: absolute; left: 0; width: 100%; top: 1316px;
    display: flex; justify-content: center; align-items: center; gap: 14px;
    font-size: 22px; letter-spacing: 1.5px; color: var(--ink);
  }
  .back-footer svg { width: 20px; height: 20px; }
  .back-footer__sep { color: var(--brand-blue); }
</style>
</head>
<body>

<section class="page page--front">
  <div class="front-strip" role="img" aria-label="Dark blue and purple abstract data light streaks"></div>
  <div class="front-visual" role="img" aria-label="Network cable plug with a glowing purple and cyan data stream"></div>

  <div class="brand-mark"><span class="brand-mark__square"></span>Brandvik Electric</div>

  <div class="front-photo" role="img" aria-label="Downtown San Francisco skyline"></div>

  <svg class="front-band" viewBox="0 0 1066 250" preserveAspectRatio="none" aria-hidden="true">
    <defs>
      <linearGradient id="frontBand" x1="0" y1="0" x2="1" y2="0">
        <stop offset="0" stop-color="#1b1450" stop-opacity="0.9"/>
        <stop offset="0.35" stop-color="#0d3f9a"/>
        <stop offset="1" stop-color="#1272c9"/>
      </linearGradient>
    </defs>
    <path d="M0,10 Q500,25 1066,0 L1066,230 Q700,195 300,205 Q120,212 0,228 Z" fill="url(#frontBand)"/>
  </svg>

  <h1 class="front-title">Data Communication &amp;<br>Low Voltage department.</h1>

  <ul class="contact-list">
    <li>
      <svg viewBox="0 0 24 24" aria-hidden="true"><circle cx="12" cy="12" r="10" fill="none" stroke="#0d4fa8" stroke-width="2.4"/><path d="M2 12h20M12 2c3 3 3 17 0 20M12 2c-3 3-3 17 0 20" fill="none" stroke="#0d4fa8" stroke-width="2"/></svg>
      brandvikelectric.example
    </li>
    <li>
      <svg viewBox="0 0 24 24" aria-hidden="true"><rect x="2" y="5" width="20" height="14" rx="1.5" fill="#0d4fa8"/><path d="M2 6l10 7 10-7" fill="none" stroke="#ffffff" stroke-width="1.6"/></svg>
      NetLink@Brandvikelectric.example
    </li>
  </ul>
</section>

<section class="page page--back">
  <div class="back-photo" role="img" aria-label="Faded panorama of downtown San Francisco"></div>

  <div class="services-panel">
    <div class="service service--pm">
      <div class="service__icon">
        <svg viewBox="0 0 40 40" aria-hidden="true"><circle cx="16" cy="12" r="7" fill="#fff"/><path d="M3 34c0-8 6-13 13-13 4 0 7 1 9 3v10z" fill="#fff"/><circle cx="30" cy="29" r="6" fill="none" stroke="#fff" stroke-width="3"/></svg>
      </div>
      <div>
        <h2 class="service__title">Project Management</h2>
        <p class="service__text">Management of voice and data installations for educational, commercial, hospitality, residential, retail, and health care institutions.</p>
      </div>
    </div>

    <div class="service service--truck">
      <div class="service__icon">
        <svg viewBox="0 0 40 40" aria-hidden="true"><rect x="3" y="10" width="21" height="18" rx="2" fill="none" stroke="#fff" stroke-width="2.6"/><path d="M24 16h7l5 6v6H24z" fill="none" stroke="#fff" stroke-width="2.6"/><circle cx="11" cy="31" r="3.5" fill="#fff"/><circle cx="30" cy="31" r="3.5" fill="#fff"/></svg>
      </div>
      <div>
        <h2 class="service__title">Service Truck</h2>
        <p class="service__text">Whether your troubleshooting needs are large or small, we have the truck, tools, and technicians to solve your problem.</p>
      </div>
    </div>

    <div class="service service--cad">
      <div class="service__icon">
        <svg viewBox="0 0 40 40" aria-hidden="true"><rect x="4" y="6" width="32" height="22" rx="2" fill="none" stroke="#fff" stroke-width="2.6"/><path d="M16 34h8M20 28v6" stroke="#fff" stroke-width="2.6"/><path d="M12 23l8-12 8 12" fill="none" stroke="#fff" stroke-width="2.2"/></svg>
      </div>
      <div>
        <h2 class="service__title">CAD</h2>
        <p class="service__text">Our CAD department can provide a quality install by providing computer‑aided as‑built drawings upon project completion, as well as printing services.</p>
      </div>
    </div>

    <div class="service service--voice">
      <div class="service__icon">
        <svg viewBox="0 0 40 40" aria-hidden="true"><rect x="15" y="7" width="10" height="18" rx="5" fill="#fff"/><path d="M10 18a10 10 0 0 0 20 0M20 28v6M14 34h12" fill="none" stroke="#fff" stroke-width="2.6"/></svg>
      </div>
      <div>
        <h2 class="service__title">Voice &amp; Data Services</h2>
        <p class="service__text">Brandvik Communications has partnered with local IT and phone vendors to offer our customers a combined solution to ensure a seamless transition.</p>
      </div>
    </div>

    <div class="service service--cabling">
      <div class="service__icon">
        <svg viewBox="0 0 40 40" aria-hidden="true"><rect x="7" y="16" width="7" height="18" fill="#fff"/><rect x="16.5" y="16" width="7" height="18" fill="#fff"/><rect x="26" y="16" width="7" height="18" fill="#fff"/><path d="M10.5 16V7M20 16V7M29.5 16V7" stroke="#fff" stroke-width="2"/></svg>
      </div>
      <div>
        <h2 class="service__title">Data/Voice/Fiber Optic Structured Cabling/CATV</h2>
        <p class="service__text">Brandvik Communications offers complete voice, data, and video infrastructure cabling services. We install Category 5e, 6, 6A, 10 Gig, and fiber optic cabling systems to meet our customers’ growing needs.</p>
      </div>
    </div>
  </div>

  <svg class="back-band" viewBox="0 0 1066 250" preserveAspectRatio="none" aria-hidden="true">
    <defs>
      <linearGradient id="backBand" x1="0" y1="0" x2="1" y2="0">
        <stop offset="0" stop-color="#0b3f98"/>
        <stop offset="1" stop-color="#1177cc"/>
      </linearGradient>
    </defs>
    <path d="M0,0 Q530,40 1066,0 L1066,230 Q530,170 0,230 Z" fill="url(#backBand)"/>
  </svg>

  <div class="emergency">
    <svg viewBox="0 0 48 48" aria-hidden="true"><path d="M4 18c4-8 36-8 40 0l-2 5-8-2v-4c-5-2-15-2-20 0v4l-8 2z" fill="#fff"/><path d="M12 24h24l4 12H8z" fill="#fff"/><rect x="6" y="40" width="36" height="3" fill="#fff"/></svg>
    <div class="emergency__lines">
      24/7 Emergency<br>Call number <span class="emergency__number">415-555-0148</span>
    </div>
  </div>

  <div class="back-footer">
    <svg viewBox="0 0 24 24" aria-hidden="true"><circle cx="12" cy="12" r="10" fill="none" stroke="#0d4fa8" stroke-width="2.4"/><path d="M2 12h20M12 2c3 3 3 17 0 20M12 2c-3 3-3 17 0 20" fill="none" stroke="#0d4fa8" stroke-width="2"/></svg>
    <span>brandvikelectric.example</span>
    <span class="back-footer__sep">|</span>
    <span>License # 573106</span>
    <span class="back-footer__sep">|</span>
    <span>Dir # 300928451</span>
  </div>
</section>

</body>
</html>
```